FAST TURN AROUND - Yoga & Sound Meditation Event Flyer

Our organization - Tarrow Guidance Alliance - is currently looking for someone to create a flyer for an upcoming Yoga & Sound Meditation Event.

We are looking for the following deliverables:
Versions of the Flyer created for Social Media (Long Story & Square Post) that includes the following information. (Not including the categories)
Event Title: Tarrow Flow & Hum Unwind Session - Bayline Mix
Event Date & Time: Wednesday, April 20 | 7P - 9P
Event Location: Reedhall at Cobbleyard
Tarrow Logo: (Both black and white versions are attached. Feel free to use whichever makes more sense based on the lighting)

We would want a version of this for the eight different background images provided. For the test, you can submit 1-2 since the rest of the details will be the same once we chose the information design.

```html
<!DOCTYPE html>
<html lang="en">
<head>
<meta charset="utf-8">
<title>Tarrow Flow &amp; Hum Unwind Session – Flyers</title>
<link href="https://fonts.googleapis.com/css2?family=Pathway+Gothic+One&family=Open+Sans:wght@400&display=swap" rel="stylesheet">
<style>
  :root{
    --stage:#3b3b3b;
    --amber:#ffab12;
    --white:#ffffff;
    --rule:#8a8078;
    --deep:#130402;
    --black:#000000;
    --ember:#c2540a;
    --rust:#5a1e05;
  }
  *{box-sizing:border-box;margin:0;padding:0}
  html,body{width:1200px;height:1200px;overflow:hidden;background:var(--stage)}
  .stage{position:relative;width:1200px;height:1200px}
  .flyer{position:absolute;overflow:hidden;background:linear-gradient(180deg,var(--deep) 0%,var(--deep) 55%,var(--black) 100%);font-family:"Pathway Gothic One",sans-serif;font-weight:400;text-align:center}
  .flyer--story{left:76px;top:154px;width:502px;height:891px}
  .flyer--square{left:625px;top:324px;width:504px;height:503px}
  .flyer__photo{position:absolute;left:0;top:0;width:100%;
    background:
      radial-gradient(ellipse 14% 9% at 50% 44%,rgba(255,170,60,.45),transparent),
      radial-gradient(ellipse 10% 5% at 4% 57%,rgba(255,120,20,.7),transparent),
      radial-gradient(ellipse 12% 6% at 94% 57%,rgba(255,140,30,.75),transparent),
      radial-gradient(ellipse 18% 14% at 88% 45%,rgba(220,110,30,.35),transparent),
      linear-gradient(180deg,var(--rust) 0%,#8a3a0c 40%,var(--ember) 55%,#2a0d04 68%,#1a0703 85%,var(--deep) 100%)}
  .flyer--story .flyer__photo{height:436px}
  .flyer--square .flyer__photo{height:298px}
  .flyer__title,.flyer__subtitle,.flyer__details,.flyer__brand,.flyer__org{font-weight:400;white-space:nowrap}
  .flyer__title{position:absolute;left:0;right:0;color:var(--amber);font-size:38px;line-height:1}
  .flyer__subtitle{position:absolute;left:0;right:0;color:var(--amber);font-size:31px;line-height:1}
  .flyer__details{position:absolute;left:16px;right:16px;display:flex;justify-content:center;align-items:stretch;color:var(--white);font-size:28px;line-height:1;border-top:1px solid var(--rule);border-bottom:1px solid var(--rule)}
  .flyer__details span{display:flex;align-items:center;flex:0 0 auto;padding:0 11px;white-space:nowrap}
  .flyer__details .flyer__divider{width:1px;padding:0;background:var(--rule)}
  .flyer__brand{position:absolute;left:0;right:0;color:var(--white);font-size:46px;line-height:1;letter-spacing:1px}
  .flyer__org{position:absolute;left:0;right:0;color:var(--white);font-family:"Open Sans",sans-serif;font-size:15px;line-height:1}
  .flyer--story .flyer__title{top:468px}
  .flyer--story .flyer__subtitle{top:508px}
  .flyer--story .flyer__details{top:553px;height:45px}
  .flyer--story .flyer__brand{top:744px}
  .flyer--story .flyer__org{top:790px}
  .flyer--square .flyer__title{top:292px}
  .flyer--square .flyer__subtitle{top:332px}
  .flyer--square .flyer__details{top:378px;height:46px}
  .flyer--square .flyer__brand{top:436px;font-size:38px}
  .flyer--square .flyer__org{top:474px;font-size:13px}
</style>
</head>
<body>
<div class="stage">
  <section class="flyer flyer--story">
    <div class="flyer__photo" role="img" aria-label="Candlelit sound meditation room with a gong player seated among people resting on mats"></div>
    <h1 class="flyer__title">Tarrow Flow &amp; Hum Unwind Session</h1>
    <h2 class="flyer__subtitle">Bayline Mix</h2>
    <p class="flyer__details"><span>Wednesday, April 20 | 7P - 9P</span><span class="flyer__divider"></span><span>Reedhall at Cobbleyard</span></p>
    <p class="flyer__brand">Tarrow</p>
    <p class="flyer__org">Tarrow Guidance Alliance</p>
  </section>
  <section class="flyer flyer--square">
    <div class="flyer__photo" role="img" aria-label="Candlelit sound meditation room with a gong player seated among people resting on mats"></div>
    <h1 class="flyer__title">Tarrow Flow &amp; Hum Unwind Session</h1>
    <h2 class="flyer__subtitle">Bayline Mix</h2>
    <p class="flyer__details"><span>Wednesday, April 20 | 7P - 9P</span><span class="flyer__divider"></span><span>Reedhall at Cobbleyard</span></p>
    <p class="flyer__brand">Tarrow</p>
    <p class="flyer__org">Tarrow Guidance Alliance</p>
  </section>
</div>
</body>
</html>
```